Pellor Autos, LLC Business Card
Business Card
Pellor Autos, LLC Business Card -
Creative Brief
Simple
Marcus Denby
Owner
4471 Brantley Ave Suite K Houston, TX 77066
pellorautosllc@brintomail.com
I want a picture of the business logo.

```html
<!DOCTYPE html>
<html lang="en">
<head>
<meta charset="utf-8">
<title>Pellor Autos, LLC Stationery</title>
<link href="https://fonts.googleapis.com/css2?family=Oswald:wght@600&family=Open+Sans:wght@400;600&display=swap" rel="stylesheet">
<style>
:root{
  --bg:#ece7df;
  --paper:#ffffff;
  --red:#b3222c;
  --red-dark:#7e1219;
  --red-soft:#e7b5b8;
  --grey:#6f6f72;
  --grey-dark:#3c3c3f;
  --ink:#2a2a2a;
  --muted:#8a8a8a;
  --faint:#eeeeee;
}
*{box-sizing:border-box;margin:0;padding:0}
html,body{width:1200px;height:346px;overflow:hidden;background:var(--bg)}
body{position:relative;font-family:"Open Sans",Arial,sans-serif;color:var(--ink)}
.piece{position:absolute;background:var(--paper);box-shadow:0 1px 3px rgba(0,0,0,.18)}
.label{position:absolute;font-size:5px;letter-spacing:.5px;color:var(--muted);text-transform:uppercase;white-space:nowrap}
.brand{display:flex;align-items:center;gap:3px;font-family:"Oswald",Arial,sans-serif;font-weight:600;color:var(--red-dark);text-transform:uppercase;white-space:nowrap}
.brand-square{width:7px;height:7px;background:var(--red)}
.small{font-size:4px;line-height:1.35;color:var(--ink)}
.rule-top{position:absolute;left:0;right:0;top:0;height:3px;background:var(--red)}
.band-bottom{position:absolute;left:0;right:0;bottom:0;height:18px;background:linear-gradient(to bottom,var(--red-soft),var(--red) 45%,var(--red-dark))}

/* business cards */
.card{left:19px;width:92px;height:53px}
.card-front{top:125px;padding:8px 7px}
.card-front .brand{font-size:8px}
.card-front .small{margin-top:5px}
.card-back{top:197px;background:linear-gradient(to right,var(--paper) 0 58%,var(--grey-dark) 58%);display:flex;align-items:center;justify-content:flex-end;padding-right:9px}
.card-back .brand{font-size:6px;color:var(--paper)}
.card-back .brand-square{background:var(--red)}
.card-back .stripe{position:absolute;left:0;top:0;bottom:0;width:58%;background:linear-gradient(var(--paper),var(--faint))}

/* letterheads */
.letterhead{top:14px;width:216px;height:318px}
.letterhead .head{position:absolute;left:12px;top:10px;right:12px;display:flex;justify-content:space-between}
.letterhead .brand{font-size:10px}
.letterhead .small{text-align:right}
.letterhead .mark{position:absolute;left:50%;top:50%;width:96px;height:96px;margin:-48px 0 0 -48px;border-radius:50%;background:var(--faint)}
.lh-one{left:139px}
.lh-two{left:372px}

/* envelopes */
.envelope{left:619px;width:226px;height:96px}
.envelope .brand{position:absolute;left:9px;top:9px;font-size:8px}
.envelope .small{position:absolute;left:9px;top:22px}
.envelope .band-bottom{height:9px}
.env-one{top:43px}
.env-two{top:160px}

.env-backs{position:absolute;left:869px;top:12px}
</style>
</head>
<body>

<div class="label" style="left:19px;top:115px">Business Card Front</div>
<section class="piece card card-front">
  <div class="brand"><span class="brand-square"></span>Pellor Autos, LLC</div>
  <p class="small"><strong>Marcus Denby</strong><br>Owner<br>4471 Brantley Ave Suite K<br>Houston, TX 77066<br>pellorautosllc@brintomail.com</p>
</section>
<div class="label" style="left:19px;top:183px">Business Card Back</div>
<section class="piece card card-back">
  <div class="stripe"></div>
  <div class="brand"><span class="brand-square"></span>Pellor</div>
</section>

<section class="piece letterhead lh-one">
  <div class="rule-top"></div>
  <div class="head">
    <div class="brand"><span class="brand-square"></span>Pellor Autos, LLC</div>
    <p class="small">4471 Brantley Ave Suite K<br>Houston, TX 77066<br>Tel (281) 555-0148<br>pellorautosllc@brintomail.com</p>
  </div>
  <div class="mark" role="img" aria-label="Faint brand mark watermark"></div>
  <div class="band-bottom"></div>
</section>
<div class="label" style="left:221px;top:337px">Letterhead Page One</div>

<section class="piece letterhead lh-two">
  <div class="rule-top"></div>
  <div class="mark" role="img" aria-label="Faint brand mark watermark"></div>
  <div class="band-bottom"></div>
</section>
<div class="label" style="left:454px;top:337px">Letterhead Page Two</div>

<section class="piece envelope env-one">
  <div class="rule-top"></div>
  <div class="brand"><span class="brand-square"></span>Pellor Autos, LLC</div>
  <p class="small">4471 Brantley Ave Suite K<br>Houston, TX 77066</p>
  <div class="band-bottom"></div>
</section>
<div class="label" style="left:700px;top:143px">Envelope Number Ten</div>

<section class="piece envelope env-two">
  <div class="rule-top"></div>
  <div class="brand"><span class="brand-square"></span>Pellor Autos, LLC</div>
  <p class="small">4471 Brantley Ave Suite K<br>Houston, TX 77066</p>
  <div class="band-bottom"></div>
</section>
<div class="label" style="left:700px;top:260px">Envelope Number Ten</div>

<svg class="env-backs" width="310" height="270" viewBox="0 0 310 270" aria-label="Envelope backs">
  <defs>
    <linearGradient id="redFlap" x1="0" y1="0" x2="0" y2="1">
      <stop offset="0" stop-color="#c7343d"/><stop offset="1" stop-color="#7e1219"/>
    </linearGradient>
    <linearGradient id="greyFlap" x1="0" y1="0" x2="0" y2="1">
      <stop offset="0" stop-color="#8a8a8d"/><stop offset="1" stop-color="#3c3c3f"/>
    </linearGradient>
  </defs>
  <polygon points="0,2 308,2 308,18 154,58 0,18" fill="url(#redFlap)"/>
  <circle cx="154" cy="36" r="7" fill="#ffffff"/>
  <polygon points="0,70 308,70 308,88 154,130 0,88" fill="url(#greyFlap)"/>
  <circle cx="154" cy="104" r="7" fill="#ffffff"/>
  <rect x="0" y="144" width="308" height="116" fill="#ffffff"/>
  <polyline points="0,146 154,196 308,146" fill="none" stroke="#d8d8d8" stroke-width="1"/>
  <polygon points="0,144 308,144 154,194" fill="#f6f6f6"/>
  <circle cx="154" cy="178" r="7" fill="#b3222c"/>
</svg>
<div class="label" style="left:975px;top:280px">Envelope Back Design View</div>

</body>
</html>
```